Homeopathic medicinal cream label design

I am looking for a product label design for a medicinal (cannabis) topical cream to be sold to medical marijuana patients. It is a new product that has not yet established a brand identity. It will be sold in 2 and 4 ounce containers so the design needs to work on a small scale. The design may be used for other branding as well.

Target Market(s)

Medical marijuana users in states where it is legal. The product should appeal to both men and women to promote pain relief in muscles and joints. It can also be used as a massage cream for general relaxation.

Industry/Entity Type

Medical

Font styles to use
Sans Serif

Requirements
Must have
• Something that reflects the company name - The Quiet Lark - and the name of the initial product - Meadow Balm Blend.
• In addition to the name of the company and the name of the product, other information to include would be the volume being sold (e.g. 4 oz.), that it is a topical botanical ointment, and its ingredients (coconut oil, beeswax, soy lecithin, and eight all natural botanical oils - cannabis, lavender, eucalyptus, peppermint, rosemary, cinnamon, clove, and lemon). The label should clearly state that the product is for topical use only.
• The information must fit on the space available on the package. The 4 oz. container's lid has approximately 2 1/8" of surface area. The width of the label on the lid should be approximately 1 7/8". On the container's body, the height of the surface area is approximately 1", and the width is approximately 8 1/2 inches. The width of the label should be around 8 inches to allow room for it to be applied to the container. I have posted a photo of the 4 oz. container and the 2 oz. container. I have also posted a photo of the labeling of some of our competitors with similar products.
Nice to have
• We are thinking of having the logo on the lid of the container, and a circle bordering the lid that may have text in it. (See the "Amber Owl" label attached as an exemplar).
• The label on the body of the container (or maybe on the bottom on the container) would list other information about the product, such as its ingredients and our contact information.

```html
<!DOCTYPE html>
<html lang="en">
<head>
<meta charset="utf-8">
<title>The Quiet Lark – Meadow Balm Blend Lid Label</title>
<link href="https://fonts.googleapis.com/css2?family=Delius&family=Fredoka:wght@600&family=Lato:wght@400&display=swap" rel="stylesheet">
<style>
  :root {
    --paper: #f7f6ee;
    --frame: #a9cf5a;
    --leaf-deep: #6fae2e;
    --leaf-mid: #9fcb45;
    --leaf-light: #cfe38a;
    --ring: #e9efcf;
    --ring-edge: #b9d57a;
    --disc: #f4f6e3;
    --title-fill: #8cc43c;
    --title-edge: #34402a;
    --ink: #3a3a38;
    --ring-ink: #5a5a52;
  }
  html, body {
    margin: 0;
    padding: 0;
    width: 1200px;
    height: 1200px;
    overflow: hidden;
    background: var(--paper);
  }
  .label {
    position: relative;
    width: 1200px;
    height: 1200px;
    background: var(--paper);
  }
  .label svg { display: block; }
  .ring-text {
    font-family: "Lato", sans-serif;
    font-size: 32px;
    fill: var(--ring-ink);
    letter-spacing: 1px;
  }
  .brand-name {
    font-family: "Delius", sans-serif;
    font-size: 50px;
    fill: var(--ink);
  }
  .product-name {
    font-family: "Fredoka", sans-serif;
    font-weight: 600;
    font-size: 86px;
    fill: var(--title-fill);
    stroke: var(--title-edge);
    stroke-width: 4px;
    paint-order: stroke fill;
    letter-spacing: 2px;
  }
  .volume {
    font-family: "Lato", sans-serif;
    font-weight: 700;
    font-size: 24px;
    fill: var(--ink);
  }
  .ingredients {
    font-family: "Lato", sans-serif;
    font-size: 22px;
    fill: var(--ink);
  }
</style>
</head>
<body>
<main class="label">
  <svg width="1200" height="1200" viewBox="0 0 1200 1200" xmlns="http://www.w3.org/2000/svg">
    <defs>
      <radialGradient id="wreath-tone" cx="50%" cy="50%" r="50%">
        <stop offset="70%" stop-color="#8fc13e"/>
        <stop offset="88%" stop-color="#a9d15a"/>
        <stop offset="100%" stop-color="#d8ea9e" stop-opacity="0"/>
      </radialGradient>
      <radialGradient id="disc-tone" cx="50%" cy="40%" r="60%">
        <stop offset="0%" stop-color="#f8f9ec"/>
        <stop offset="100%" stop-color="#eaf0d2"/>
      </radialGradient>
      <path id="ring-path" d="M 600,212 A 388,388 0 1 1 599.9,212"/>
    </defs>

    <!-- thin outer frame -->
    <rect class="frame" x="20" y="20" width="1160" height="1160" fill="none" stroke="var(--frame)" stroke-width="3"/>

    <!-- leaf wreath area -->
    <circle class="leaf-wreath" cx="600" cy="600" r="545" fill="url(#wreath-tone)"
            role="img" aria-label="Wreath of green botanical leaves surrounding the label"/>

    <!-- outer ring band -->
    <circle class="ring-band" cx="600" cy="600" r="432" fill="var(--ring)" stroke="var(--ring-edge)" stroke-width="3"/>

    <!-- inner disc -->
    <circle class="center-disc" cx="600" cy="600" r="360" fill="url(#disc-tone)" stroke="var(--ring-edge)" stroke-width="3"/>

    <!-- ring text -->
    <text class="ring-text">
      <textPath href="#ring-path" textLength="2430" lengthAdjust="spacing">Topical Botanical Ointment  ·  Topical Botanical Ointment  ·  Topical Botanical Ointment  ·</textPath>
    </text>

    <!-- brand mark placeholder -->
    <circle class="brand-dot" cx="600" cy="350" r="52" fill="var(--leaf-light)"/>

    <!-- brand name -->
    <text class="brand-name" x="600" y="526" text-anchor="middle">the quiet lark</text>

    <!-- product name -->
    <text class="product-name" x="600" y="632" text-anchor="middle">MEADOW</text>
    <text class="product-name" x="600" y="730" text-anchor="middle">BALM BLEND</text>

    <!-- volume -->
    <text class="volume" x="890" y="768" text-anchor="end">4oz.</text>

    <!-- ingredients -->
    <text class="ingredients" text-anchor="middle">
      <tspan x="600" y="818">coconut oil, beeswax, soy lecithin, and eight all</tspan>
      <tspan x="600" y="850">natural botanical oils - cannabis, lavender,</tspan>
      <tspan x="600" y="882">eucalyptus, peppermint, rosemary,</tspan>
      <tspan x="600" y="914">cinnamon, clove, and lemon</tspan>
    </text>
  </svg>
</main>
</body>
</html>
```